Home builder needs an eyecatching brochure to generate more leads

We need an A5 bifold brochure (4 pages) designed using our professional images of our projects. We would like to see a good use of colour that works with our brand colours (as used in our logo) and that makes the images really stand out. We will need to include some text and want the overall feel of the brochure to be informative and visually appealing. Our biggest element we need to convey to prospective clients is trust.
We will use these brochures in a holder on our site signage (at the front of current building projects) to generate interest in the immediate area, and also to give to prospective clients at our first consultation. I can supply an image of the site sign we will be adhering the brochure holder to.
I have included some copy which can be used, but it doesnt all need to be included in the brochure. Also I have uploaded 6 images but they dont all need to be used. I feel larger images will have more impact so that may mean not using them all.
Updates

Dear Designers
I have now added the QR code  (added to the uploads in the brief) that I wish to appear on my brochure. This leads to a Youtube video of some client testimonials. I think some text along the lines of "Here is a video showing what our clients say about us" near this QR code. If you have a better invitation to view the video, please feel free to show it in your design.

Marissa Hadley

For all those designers who have submitted so far, thank you. For any designers yet to submit, I did neglect to say in my brief, that the design  will need to be portrait orientation, and the 4 pages are front and back cover and 2 inside ie, an A4 sheet printed on both sides and folded to make A5.

Also I would prefer not to use images that are not our own, for credibility reasons. if you need to see more images, I am able to send you more. Please ask.

Many thanks
Marissa Hadley

Target Market(s)

Age groups are 40-60 year olds, both male and female, well educated, generally professionals, business owners or successful tradespeople of middle income. Our target market care about their home and need to find a builder that will care about it as much as them. They are not likely to choose a builder just because he is the cheapest.

Industry/Entity Type

Building

Requirements
Must have
• We really want to emphasise our project photos and also include a testimonials snippets from our clients. We also will supply a QR code later in the contest.
We must also include our website address www.brockfieldhomes.example.au
and email address info@brockfieldhomes.example.au and a call to action to ring us(this is included in our copy upload)

```html
<!DOCTYPE html>
<html lang="en">
<head>
<meta charset="utf-8">
<title>Brockfield Homes Brochure Spread</title>
<link rel="stylesheet" href="https://fonts.googleapis.com/css2?family=Mulish:ital,wght@0,300;1,300&family=Questrial&display=swap">
<style>
  :root {
    --brand-yellow: #f9c51a;
    --ink: #222222;
    --body-text: #555555;
    --paper: #ffffff;
    --canvas: #ffffff;
    --rule: #111111;
    --fold: #9a9a9a;
  }
  * { box-sizing: border-box; margin: 0; padding: 0; }
  html, body { width: 1200px; height: 900px; overflow: hidden; background: var(--canvas); }
  body { font-family: "Questrial", "Century Gothic", sans-serif; position: relative; }

  .spread {
    position: absolute; left: 30px; top: 50px; width: 1138px; height: 804px;
    background: var(--paper);
    box-shadow: 0 0 4px rgba(0,0,0,0.35);
    overflow: hidden;
  }
  .page { position: absolute; top: 0; height: 804px; }
  .page--left { left: 0; width: 568px; }
  .page--right { left: 570px; width: 568px; }
  .fold-line {
    position: absolute; left: 568px; top: 0; height: 804px; width: 0;
    border-left: 1px dashed var(--fold);
  }

  .headline-band {
    position: absolute; left: 0; width: 100%;
    background: var(--brand-yellow);
    border-top: 2px solid var(--rule);
    border-bottom: 4px solid var(--rule);
    padding: 6px 0 0 58px;
  }
  .headline {
    font-family: "Mulish", "Century Gothic", sans-serif;
    font-weight: 300; font-style: italic; font-size: 23px; line-height: 26px;
    color: var(--ink); letter-spacing: -0.3px;
  }
  .copy {
    position: absolute; left: 58px; width: 456px;
    font-size: 12px; line-height: 15px; color: var(--body-text);
    text-align: justify;
  }
  .copy p + p { margin-top: 14px; }

  .yellow-rule { position: absolute; left: 0; width: 100%; height: 2px; background: var(--brand-yellow); }

  .photo { position: absolute; }
  .photo--bathroom { left: 2px; top: 258px; width: 276px; height: 189px;
    background: linear-gradient(160deg, #d9d7d3 0%, #c4c0ba 45%, #9f9a93 100%); }
  .photo--kitchen { left: 281px; top: 258px; width: 287px; height: 189px;
    background: linear-gradient(170deg, #e6e4e0 0%, #c9c3bb 55%, #8a5a36 100%); }
  .photo--living { left: 0; top: 296px; width: 568px; height: 347px;
    background: linear-gradient(100deg, #6e5a48 0%, #a08468 30%, #8a4f2a 60%, #b8a48c 85%, #7a6a5a 100%); }

  .cta-panel {
    position: absolute; left: 0; top: 646px; width: 100%; height: 158px;
    background: #000; color: var(--brand-yellow);
    text-align: center; font-size: 16px; line-height: 19.5px;
    padding-top: 15px;
  }
  .cta-panel .gap { height: 19px; }
</style>
</head>
<body>
<main class="spread">
  <section class="page page--left">
    <div class="headline-band" style="top:78px;height:96px;">
      <h2 class="headline">How do you know you’ve found the right<br>builder for your new custom home, home<br>renovation or home extension?</h2>
    </div>
    <div class="copy" style="top:191px;">
      <p>You’ve found the right custom home builder when they’re happy to answer all your questions on the spot. By dealing direct with Brockfield Homes, you experience a transparent process from project concept to building completion.</p>
    </div>
    <div class="yellow-rule" style="top:256px;"></div>
    <div class="photo photo--bathroom" role="img" aria-label="Project photo: white bathroom with freestanding bath and vanity"></div>
    <div class="photo photo--kitchen" role="img" aria-label="Project photo: white kitchen with island bench and timber floor"></div>
    <div class="yellow-rule" style="top:447px;"></div>
    <div class="copy" style="top:469px;">
      <p>Raising standards in the custom home building industry. With over 22 years of building experience in custom home building, home extensions and renovations, we are certain to deliver building work that preserves the structural integrity of your home and lasts a lifetime.</p>
    </div>
    <div class="headline-band" style="top:550px;height:97px;">
      <h2 class="headline">Why is a home extension or renovation<br>the smartest lifestyle decision you<br>will ever make?</h2>
    </div>
    <div class="copy" style="top:664px;">
      <p>You spend roughly 12 hours a day in your home, more if you are working from home, bringing up children or retired. A smart home extension or renovation can add years of enjoyment to your experience of living in the home and area that you know.</p>
      <p>If your home is a bit older, it might need a facelift or some design changes to make it more energy savvy and comfortable in each season.</p>
    </div>
  </section>

  <div class="fold-line"></div>

  <section class="page page--right">
    <div class="headline-band" style="top:78px;height:96px;">
      <h2 class="headline">Imagine working with a custom home<br>builder who listens and understands what<br>you really want in your new home.</h2>
    </div>
    <div class="copy" style="top:191px;">
      <p>Having a new home built can be one of the biggest life changes you ever face. One of the biggest fears is cost blow-outs and shifting completion dates.</p>
      <p>With years of experience in managing custom home building projects, we take the fear and worry out of this big life change by giving you a fixed price and working to tight deadlines.</p>
    </div>
    <div class="yellow-rule" style="top:294px;"></div>
    <div class="photo photo--living" role="img" aria-label="Project photo: living room with stone fireplace, timber floor and dining area"></div>
    <div class="yellow-rule" style="top:643px;height:3px;"></div>
    <div class="cta-panel">
      <p>Call us now and tell us your building ideas and dreams:</p>
      <p>03 9000 4182</p>
      <p>(Ask for Marissa)</p>
      <div class="gap"></div>
      <p>Or email us at:</p>
      <p>info@brockfieldhomes.example.au</p>
    </div>
  </section>
</main>
</body>
</html>
```